Upgrade/"Tweak" My Landing Page

We need to "tweak" our current landing page. I'm a perfectionist and something seems "off". Things I LOVE about our current page: I love our message that "ONE SIZE DOES NOT FIT ALL", as well as the photo used (boy wearing an oversized hat). I also like the fact that the photo is in full screen mode- I like this look.
THINGS I DON'T Like: The font & location of our message "ONE SIZE DOES NOT FIT ALL" - just seems "off". I'm also concerned about the placement of our menu being on the left hand side of the screen. Not sure if this is ideal. Also, my product types are listed on the left hand side of the screen in the menu section. My audience seems to think these are links when in fact they are just examples of the products I sell. How can I position these so the audience knows it's for informational purposes only.
Help!! I want my landing page to be PERFECT.

```html
<!DOCTYPE html>
<html lang="en">
<head>
<meta charset="utf-8">
<title>Harborline Insurance Agency</title>
<link rel="stylesheet" href="https://fonts.googleapis.com/css2?family=Oswald:wght@300;400&family=Roboto:wght@300;400;500;700&family=Open+Sans:wght@600&display=swap">
<style>
  :root {
    --navy: #0f2456;
    --navy-deep: #061530;
    --ink: #1a2a5a;
    --white: #ffffff;
    --band: #f5f5f5;
    --rule: #e2e2e2;
    --muted: #8a8a8a;
    --icon: #9a9a9a;
    --accent: #e8304a;
    --phone: #f0616e;
    --sky-top: #5f94d9;
    --sky-bottom: #a9c8ec;
    --social-a: #3b5b9a;
    --social-b: #1a7fc0;
  }
  * { box-sizing: border-box; margin: 0; padding: 0; }
  html, body { width: 1200px; height: 1000px; overflow: hidden; background: var(--white); }
  body { position: relative; font-family: "Roboto", Arial, sans-serif; }

  .brand { position: absolute; top: 18px; left: 0; width: 1200px; text-align: center; color: var(--navy); }
  .brand-dot { width: 40px; height: 40px; border-radius: 50%; background: var(--navy); margin: 0 auto 6px; }
  .brand-name { font-family: "Roboto", Arial, sans-serif; font-weight: 700; font-size: 15px; line-height: 17px; letter-spacing: 0.2px; }

  .main-nav { position: absolute; top: 110px; left: 168px; width: 879px; height: 40px; background: var(--navy);
    display: flex; justify-content: center; align-items: center; gap: 17px;
    font-family: "Open Sans", Arial, sans-serif; font-weight: 600; font-size: 11px; color: var(--white); }
  .main-nav .sep { opacity: 0.9; }

  .hero { position: absolute; top: 150px; left: 168px; width: 879px; height: 414px;
    background: linear-gradient(180deg, var(--sky-top) 0%, var(--sky-bottom) 100%); }
  .hero-photo { position: absolute; inset: 0; }
  .social { position: absolute; top: 8px; right: 95px; display: flex; gap: 6px; }
  .social span { width: 24px; height: 24px; display: block; }
  .social .s1 { background: var(--social-a); }
  .social .s2 { background: var(--social-b); }
  .hero-copy { position: absolute; top: 272px; left: 0; width: 100%; text-align: center; color: var(--white); }
  .hero-title { font-family: "Oswald", "Arial Narrow", sans-serif; font-weight: 300; font-size: 58px; line-height: 64px; letter-spacing: -1px; transform: scaleX(0.88); }
  .hero-sub { font-weight: 700; font-size: 20px; line-height: 24px; margin-top: 0; text-shadow: 0 1px 2px rgba(0,0,0,0.25); }
  .hero-btn { display: inline-block; margin-top: 14px; width: 107px; height: 26px; border: 1.5px solid var(--white);
    font-size: 13px; line-height: 23px; letter-spacing: 0.3px; }

  .products-head { position: absolute; top: 564px; left: 168px; width: 879px; height: 80px; background: var(--band);
    border-bottom: 1px solid var(--rule); text-align: center; font-weight: 300; font-size: 21px; line-height: 82px; color: var(--muted); }

  .products { position: absolute; top: 665px; left: 0; width: 1200px; height: 80px; }
  .product { position: absolute; top: 0; height: 78px; text-align: center; }
  .product-label { font-weight: 500; font-size: 10.5px; line-height: 10px; color: var(--accent); letter-spacing: 0.1px; }
  .product svg { position: absolute; left: 50%; transform: translateX(-50%); top: 40px; }
  .divider { position: absolute; top: 0; width: 1px; height: 78px; background: var(--rule); }

  .cta { position: absolute; top: 763px; left: 169px; width: 878px; height: 165px;
    background: linear-gradient(90deg, var(--navy-deep) 0%, var(--navy-deep) 7%, #102a5e 12%, #0d2350 60%, #0a1d40 100%);
    text-align: center; color: var(--white); }
  .cta-text { position: absolute; top: 42px; left: 0; width: 100%; font-weight: 300; font-size: 16.5px; line-height: 23px; }
  .cta-phones { position: absolute; top: 100px; left: 0; width: 100%; display: flex; justify-content: center; align-items: center; gap: 10px;
    font-weight: 300; font-size: 22px; color: var(--phone); }
  .cta-phones .slash { color: var(--white); }

  .site-footer { position: absolute; top: 953px; left: 0; width: 1200px; text-align: center; }
  .footer-links { font-size: 9.5px; color: var(--ink); line-height: 12px; }
  .copyright { font-size: 8.5px; color: #777; margin-top: 4px; }
</style>
</head>
<body>

<header class="brand">
  <div class="brand-dot"></div>
  <div class="brand-name">HARBORLINE INSURANCE<br>AGENCY</div>
</header>

<nav class="main-nav">
  <span>About us</span><span class="sep">|</span>
  <span>Pay your bill</span><span class="sep">|</span>
  <span>Request a quote or policy change</span><span class="sep">|</span>
  <span>File a claim</span><span class="sep">|</span>
  <span>Contact us</span>
</nav>

<section class="hero">
  <div class="hero-photo" role="img" aria-label="Photo of a child seen from behind wearing an oversized red sun hat against a clear blue sky"></div>
  <div class="social"><span class="s1"></span><span class="s2"></span></div>
  <div class="hero-copy">
    <h1 class="hero-title">ONE SIZE DOES NOT FIT ALL</h1>
    <p class="hero-sub">Custom-made solutions at your fingertips</p>
    <span class="hero-btn">KNOW MORE</span>
  </div>
</section>

<h2 class="products-head">Our Insurance Products</h2>

<section class="products">
  <div class="product" style="left:241px;width:60px"><div class="product-label">HOME</div>
    <svg width="26" height="24" viewBox="0 0 26 24"><path d="M13 2 L1 13 H5 V23 H11 V16 H15 V23 H21 V13 H25 Z" fill="var(--icon)"/></svg></div>
  <div class="divider" style="left:304px"></div>
  <div class="product" style="left:309px;width:60px"><div class="product-label">CONDO</div>
    <svg width="20" height="32" viewBox="0 0 20 32" style="top:38px"><rect x="1" y="1" width="18" height="30" fill="var(--icon)"/><g fill="#fff"><rect x="4" y="5" width="4" height="3"/><rect x="12" y="5" width="4" height="3"/><rect x="4" y="11" width="4" height="3"/><rect x="12" y="11" width="4" height="3"/><rect x="4" y="17" width="4" height="3"/><rect x="12" y="17" width="4" height="3"/><rect x="8" y="24" width="4" height="7"/></g></svg></div>
  <div class="divider" style="left:371px"></div>
  <div class="product" style="left:376px;width:70px"><div class="product-label">BUSINESS</div>
    <svg width="22" height="20" viewBox="0 0 22 20" style="top:48px"><rect x="7" y="1" width="8" height="5" fill="none" stroke="var(--icon)" stroke-width="2"/><rect x="1" y="5" width="20" height="14" rx="2" fill="var(--icon)"/></svg></div>
  <div class="divider" style="left:449px"></div>
  <div class="product" style="left:456px;width:80px"><div class="product-label">WINDSTORM</div>
    <svg width="30" height="28" viewBox="0 0 30 28" style="top:44px"><path d="M7 16 a5 5 0 0 1 1-10 a7 7 0 0 1 13 1 a5 5 0 0 1 1 9 Z" fill="var(--icon)"/><path d="M6 20 H22 M10 24 H26" stroke="var(--icon)" stroke-width="1.5" fill="none"/></svg></div>
  <div class="divider" style="left:543px"></div>
  <div class="product" style="left:548px;width:52px"><div class="product-label">FLOOD</div>
    <svg width="24" height="28" viewBox="0 0 24 28" style="top:44px"><path d="M12 1 L2 10 H5 V17 H19 V10 H22 Z" fill="var(--icon)"/><path d="M1 21 q3-3 5.5 0 t5.5 0 t5.5 0 t5.5 0 M1 26 q3-3 5.5 0 t5.5 0 t5.5 0 t5.5 0" stroke="var(--icon)" stroke-width="2" fill="none"/></svg></div>
  <div class="divider" style="left:602px"></div>
  <div class="product" style="left:605px;width:50px"><div class="product-label">CAR</div>
    <svg width="28" height="22" viewBox="0 0 28 22" style="top:46px"><path d="M5 9 L8 3 H20 L23 9 H26 V17 H2 V9 Z" fill="none" stroke="var(--icon)" stroke-width="2"/><circle cx="8" cy="18" r="3" fill="var(--icon)"/><circle cx="20" cy="18" r="3" fill="var(--icon)"/><rect x="9" y="5" width="10" height="4" fill="var(--icon)"/></svg></div>
  <div class="divider" style="left:657px"></div>
  <div class="product" style="left:660px;width:55px"><div class="product-label">BOAT</div>
    <svg width="26" height="28" viewBox="0 0 26 28" style="top:42px"><path d="M13 2 V18 H5 Z" fill="var(--icon)"/><path d="M15 6 L21 18 H15 Z" fill="var(--icon)"/><path d="M1 20 H25 L21 26 H5 Z" fill="var(--icon)"/></svg></div>
  <div class="divider" style="left:717px"></div>
  <div class="product" style="left:722px;width:95px"><div class="product-label">MOTORCYCLE</div>
    <svg width="36" height="22" viewBox="0 0 36 22" style="top:48px"><circle cx="7" cy="15" r="5.5" fill="none" stroke="var(--icon)" stroke-width="2"/><circle cx="29" cy="15" r="5.5" fill="none" stroke="var(--icon)" stroke-width="2"/><path d="M7 15 L13 7 H22 L26 4 L29 15 M13 7 L17 14 H24" stroke="var(--icon)" stroke-width="2" fill="none"/><path d="M12 6 H23 L20 11 H14 Z" fill="var(--icon)"/></svg></div>
  <div class="divider" style="left:819px"></div>
  <div class="product" style="left:832px;width:120px"><div class="product-label">PERSONAL UMBRELLA<br>POLICY</div>
    <svg width="24" height="26" viewBox="0 0 24 26" style="top:46px"><path d="M1 11 a11 10 0 0 1 22 0 Z" fill="var(--icon)"/><path d="M12 11 V21 a2.5 2.5 0 0 1 -5 0" stroke="var(--icon)" stroke-width="1.8" fill="none"/></svg></div>
</section>

<section class="cta" role="img" aria-label="Dark blue toned photo of a city skyline of tall buildings">
  <p class="cta-text">If you are looking for a team that is highly experienced and knowledgeable, and<br>one who will be honest with you about your insurance needs, let’s talk!</p>
  <div class="cta-phones">
    <svg width="22" height="22" viewBox="0 0 22 22"><circle cx="11" cy="11" r="9.5" fill="none" stroke="var(--white)" stroke-width="1.5"/><path d="M7.5 6 L9.5 8.5 L8.5 10 Q10 12.5 12 13.5 L13.5 12.5 L16 14.5 L14.5 16.2 Q9 15.5 6 8 Z" fill="var(--white)"/></svg>
    <span>800.555.0142</span><span class="slash">/</span><span>713.555.0178</span>
  </div>
</section>

<footer class="site-footer">
  <p class="footer-links">Home / About us / Pay your bill / Request a quote or policy change / File a claim / Contact us</p>
  <p class="copyright">© Harborline Insurance Agency, 2015. All rights reserved.</p>
</footer>

</body>
</html>
```